Rare Glow Edibles Gummies

Packaging design for custom mylars for cannabis infused gummies. I need a space for a warning label, nutrition facts, ingredients, brand logo and then individualized item details. We will later be doing assorted peanut butter cups, hard candies, etc.

```html
<!DOCTYPE html>
<html lang="en">
<head>
<meta charset="utf-8">
<title>Rare Glow Edibles – Cannabis Infused Gummies Pouch</title>
<link rel="stylesheet" href="https://fonts.googleapis.com/css2?family=Kaushan+Script&family=Alfa+Slab+One&family=Open+Sans:wght@400;600&display=swap">
<style>
  :root {
    --stage-red: #c40f16;
    --pouch-red: #9e1116;
    --pouch-deep: #6e0a0e;
    --pouch-shine: #d8343a;
    --band-dark: #2a0506;
    --silver: #e9e9ec;
    --silver-shade: #b8b8bd;
    --ink-dark: #1c0a0a;
    --ribbon-green: #b7cc3a;
    --ribbon-text: #a3141a;
    --badge-white: #ffffff;
    --badge-text: #5a5a5a;
  }
  * { box-sizing: border-box; margin: 0; padding: 0; }
  html, body {
    width: 1200px; height: 985px; overflow: hidden;
    background: var(--stage-red);
  }
  .canvas { position: relative; width: 1200px; height: 985px; }

  .pouch {
    position: absolute; left: 315px; top: 42px;
    width: 570px; height: 900px;
    border-radius: 22px 22px 34px 34px;
    background:
      linear-gradient(100deg, rgba(255,255,255,0) 30%, rgba(255,120,120,0.22) 48%, rgba(255,255,255,0) 62%),
      linear-gradient(90deg, var(--pouch-deep) 0%, var(--pouch-red) 10%, var(--pouch-shine) 40%, var(--pouch-red) 75%, var(--pouch-deep) 100%);
    overflow: hidden;
    box-shadow: 0 20px 40px rgba(60,0,0,0.35);
  }
  .pouch__seal {
    position: absolute; left: 28px; right: 28px; top: 8px; height: 24px;
    background: repeating-linear-gradient(45deg, #7a0c10 0 3px, #a3161b 3px 6px);
    border-radius: 3px;
  }
  .pouch__zip {
    position: absolute; left: 22px; right: 22px; top: 104px; height: 12px;
    border-radius: 6px;
    background: linear-gradient(180deg, #e0494e, #8a0d12);
  }

  .brand {
    position: absolute; left: 80px; top: 164px;
    width: 84px; height: 84px; border-radius: 50%;
    border: 1.5px solid var(--silver);
  }
  .brand__name {
    position: absolute; left: 92px; top: 194px;
    font-family: "Open Sans", sans-serif; font-weight: 600;
    font-size: 17px; line-height: 1.05; color: var(--silver);
    width: 110px;
  }

  .mascot {
    position: absolute; left: 402px; top: 155px;
    width: 112px; height: 145px;
    border-radius: 45% 45% 50% 50% / 35% 35% 65% 65%;
    background: radial-gradient(circle at 45% 40%, #e2282e, #b3121a 70%);
    border: 3px solid var(--ink-dark);
  }

  .title {
    position: absolute; left: 60px; width: 480px; top: 290px;
    text-align: center;
    font-family: "Kaushan Script", cursive;
    font-size: 118px; line-height: 1;
    color: var(--silver);
    -webkit-text-stroke: 3px var(--ink-dark);
    text-shadow: 4px 4px 0 var(--ink-dark);
  }
  .subtitle {
    position: absolute; left: 170px; width: 340px; top: 432px;
    text-align: center;
    font-family: "Alfa Slab One", serif;
    font-size: 29px; letter-spacing: 0.5px;
    color: var(--silver);
  }

  .gummies {
    position: absolute; left: 118px; top: 505px;
    width: 388px; height: 198px;
    border-radius: 50% 50% 45% 45% / 55% 55% 45% 45%;
    background: linear-gradient(100deg, #e7b03a 0%, #6f9a2c 25%, #c41d22 50%, #e3612a 72%, #d9c43a 100%);
  }

  .badge {
    position: absolute; left: 80px; top: 645px;
    width: 84px; height: 120px;
    background: var(--badge-white);
    border-radius: 4px 4px 26px 4px;
    padding: 8px 0 0 8px;
    font-family: "Open Sans", sans-serif; font-size: 17px;
    line-height: 1.3; color: var(--badge-text);
  }
  .badge__fruit {
    position: absolute; left: 18px; bottom: 12px;
    width: 40px; height: 40px; border-radius: 40% 40% 50% 50%;
    background: linear-gradient(160deg, #e03c42, #a81218);
  }

  .ribbon {
    position: absolute; left: 313px; top: 733px;
    width: 257px; height: 41px;
  }
  .ribbon__label {
    position: absolute; left: 50px; top: 0; height: 41px; line-height: 43px;
    font-family: "Open Sans", sans-serif; font-weight: 600;
    font-size: 22px; letter-spacing: 1.5px; color: var(--ribbon-text);
  }

  .footer-rule {
    position: absolute; left: 0; right: 0; top: 789px; height: 5px;
    background: var(--silver);
  }
  .footer {
    position: absolute; left: 0; right: 0; top: 796px; bottom: 0;
    background: linear-gradient(90deg, #4a0a0c, var(--band-dark) 20%, #120203 60%, #3a0709);
    text-align: center; color: var(--silver);
    font-family: "Open Sans", sans-serif;
  }
  .footer__tagline {
    margin-top: 10px; font-size: 19px; letter-spacing: 1.2px;
  }
  .footer__ingredients {
    margin: 12px auto 0; width: 420px;
    font-size: 9.5px; line-height: 1.4;
  }
</style>
</head>
<body>
<main class="canvas">
  <section class="pouch" aria-label="Cannabis infused gummies pouch front">
    <div class="pouch__seal"></div>
    <div class="pouch__zip"></div>

    <div class="brand"></div>
    <p class="brand__name">Rare Glow Edibles</p>

    <div class="mascot" role="img" aria-label="Cartoon strawberry mascot"></div>

    <h1 class="title">Cannabis</h1>
    <p class="subtitle">INFUSED GUMMIES</p>

    <div class="gummies" role="img" aria-label="Pile of colourful fruit gummies"></div>

    <div class="badge">
      FROOT<br>CANDY
      <div class="badge__fruit" role="img" aria-label="Strawberry"></div>
    </div>

    <div class="ribbon">
      <svg width="257" height="41" viewBox="0 0 257 41" aria-hidden="true">
        <polygon points="0,0 257,0 257,41 0,41 28,20.5" fill="var(--ribbon-green)"/>
      </svg>
      <span class="ribbon__label">BERRY TWIST</span>
    </div>

    <div class="footer-rule"></div>
    <footer class="footer">
      <p class="footer__tagline">CANDY FILLED WITH REAL STRAWBERRY</p>
      <p class="footer__ingredients">INGREDIENT. THE CATEGORY, CALLED SUGAR CONFECTIONERY, ENCOMPASSES ANY SWEET CONFECTION, INCLUDING CHOCOLATE, CHEWING GUM, AND SUGAR CANDY</p>
    </footer>
  </section>
</main>
</body>
</html>
```